Printer Cartridges Supplier Namecard

Attached is my company logo and the design of my current namecard. I would like to have a more special look for it. Can have a little cuteness too rather than those normal standard feel. I'm a supplier mainly dealing with original and compatible printer toner cartridges, some other products like paper supplies as well.

Target Market(s)

Companies, businesses, corporates

Industry/Entity Type

It Company

Contact Information for Business Card

Logo, name, contact, address, supplies and maybe a slogan

Colors
85cae6
33a6d7
3176b5
0255a3
0792cd
85abd2

Requirements
Must have
• Logo, name, contact and address basic details.
• Must include some pictures, not just rearrange what I'm currently having.
Nice to have
• Be creative and bold, a diiferent traditional feel.

```html
<!DOCTYPE html>
<html lang="en">
<head>
<meta charset="utf-8">
<title>tonerbay — namecard</title>
<link rel="stylesheet" href="https://fonts.googleapis.com/css2?family=Lato:wght@300;400;700&display=swap">
<style>
  :root {
    --stage: #1f1f1f;
    --card-white: #ffffff;
    --brand-blue: #62b5e5;
    --ink-grey: #4a4a4c;
    --band-grey: #58595b;
    --rule-grey: #8a8a8a;
    --text-dark: #3c3c3c;
    --white: #ffffff;
  }
  * { margin: 0; padding: 0; box-sizing: border-box; }
  html, body { width: 1200px; height: 900px; overflow: hidden; }
  body {
    background: var(--stage);
    font-family: "Lato", sans-serif;
    position: relative;
  }
  .card {
    position: absolute;
    top: 306px;
    width: 440px;
    height: 271px;
    border-radius: 12px;
    overflow: hidden;
    box-shadow: 0 4px 10px rgba(0,0,0,0.5);
  }
  .card-front { left: 149px; background: var(--card-white); }
  .card-back { left: 608px; background: var(--brand-blue); }

  .brand {
    position: absolute;
    display: flex;
    align-items: center;
    gap: 12px;
  }
  .brand-mark { width: 50px; height: 50px; border-radius: 8px; }
  .brand-name { font-weight: 400; font-size: 50px; line-height: 1; letter-spacing: 0.5px; }

  .card-front .brand { right: 22px; top: 53px; }
  .card-front .brand-mark { background: var(--brand-blue); }
  .card-front .brand-name { color: var(--ink-grey); }

  .holder-name {
    position: absolute; left: 21px; top: 142px;
    color: var(--brand-blue); font-size: 22px; font-weight: 400;
  }
  .holder-role {
    position: absolute; left: 21px; top: 165px;
    color: var(--text-dark); font-size: 13px;
  }
  .name-rule {
    position: absolute; left: 116px; right: 23px; top: 172px;
    height: 1px; background: var(--rule-grey);
  }
  .contact-list {
    position: absolute; left: 22px; top: 197px;
    list-style: none; font-size: 13px; color: var(--text-dark);
  }
  .contact-list li { display: flex; align-items: center; gap: 6px; height: 16.5px; }
  .contact-list svg { width: 9px; height: 9px; fill: var(--brand-blue); }
  .address {
    position: absolute; right: 25px; top: 214px;
    text-align: right; font-size: 13px; color: var(--text-dark); line-height: 16.5px;
    font-style: normal;
  }

  .card-back .brand { left: 84px; top: 76px; }
  .card-back .brand-mark { background: var(--white); }
  .card-back .brand-name { color: var(--white); }
  .tagline {
    position: absolute; left: 176px; top: 131px;
    color: var(--white); font-size: 9px;
  }
  .service-band {
    position: absolute; left: 0; right: 0; top: 182px; height: 67px;
    background: var(--band-grey);
    display: grid; grid-template-columns: 195px auto;
    align-content: center; padding-left: 30px; padding-top: 3px; row-gap: 1px;
    list-style: none; color: var(--white); font-size: 13px;
  }
  .service-band li { display: flex; align-items: center; gap: 5px; }
  .service-band li::before {
    content: ""; width: 7px; height: 7px; border-radius: 50%; background: var(--white);
  }
</style>
</head>
<body>
  <section class="card card-front">
    <div class="brand">
      <span class="brand-mark"></span>
      <span class="brand-name">tonerbay</span>
    </div>
    <h1 class="holder-name">Mara Lindholm</h1>
    <p class="holder-role">Sales Executive</p>
    <div class="name-rule"></div>
    <ul class="contact-list">
      <li><svg viewBox="0 0 10 10"><rect x="2" y="0" width="6" height="10" rx="1"/><rect x="3" y="1.2" width="4" height="6.5" fill="#fff"/></svg>9000 1357</li>
      <li><svg viewBox="0 0 10 10"><rect x="0" y="1.5" width="10" height="7" rx="0.8"/><path d="M0.6 2.2 L5 5.6 L9.4 2.2" stroke="#fff" stroke-width="1" fill="none"/></svg>mara@tonerbay.sg</li>
      <li><svg viewBox="0 0 10 10"><circle cx="5" cy="5" r="5"/></svg>www.tonerbay.sg</li>
    </ul>
    <address class="address">14 Harbourline Road<br>#05-112, Singapore 500000</address>
  </section>

  <section class="card card-back">
    <div class="brand">
      <span class="brand-mark"></span>
      <span class="brand-name">tonerbay</span>
    </div>
    <p class="tagline">Compatible printer ink and toner solutions</p>
    <ul class="service-band">
      <li>Printer Ink &amp; Toner Cartridges</li>
      <li>Paper Products</li>
      <li>Original Printer Cartridges</li>
      <li>Printer Maintainence &amp; Repair</li>
    </ul>
  </section>
</body>
</html>
```